A Speech Therapy Business needs to update their logo

I need an update to the font and color of my logo to look more appealing. I am looking to open a private practice as a Speech Language Pathologist that caters to adults and children. It needs to be sophisticated and friendly at the same time. I want to keep the silhouette in my logo as is, just update the font and color for "Brightpaths".
Industry/Entity Type
Business
Contact Information for Business Card
I want the business card to have my logo, my name (Dorota Valk, CCC-SLP, TSSLD) and that I am a Bilingual Speech Language Pathologist. Also, include my phone number, (555) 271-8390. Include my website, Brightpathsslp.example, and email address, dorotavalk@brightpathsslp.example
Look and feel
Each slider illustrates characteristics of the customer's brand and the style your logo design should communicate.

```html
<!DOCTYPE html>
<html lang="en">
<head>
<meta charset="utf-8">
<title>Brightpaths — Business Card</title>
<link rel="stylesheet" href="https://fonts.googleapis.com/css2?family=Rubik:wght@400;500&display=swap">
<style>
  :root {
    --backdrop: #2a2b30;
    --card: #ffffff;
    --brand-purple: #7a5ea8;
    --text-grey: #8a8a8a;
    --logo-text: #ffffff;
  }
  * { box-sizing: border-box; margin: 0; padding: 0; }
  html, body {
    width: 1200px;
    height: 900px;
    overflow: hidden;
    background: var(--backdrop);
    font-family: "Rubik", sans-serif;
  }
  .canvas {
    position: relative;
    width: 1200px;
    height: 900px;
  }
  .business-card {
    position: absolute;
    left: 100px;
    top: 165px;
    width: 1000px;
    height: 570px;
    background: var(--card);
    box-shadow: 0 18px 40px rgba(0, 0, 0, 0.45);
  }
  .brand-mark {
    position: absolute;
    left: 70px;
    top: 100px;
    width: 370px;
    height: 370px;
    border-radius: 50%;
    background: var(--brand-purple);
    display: flex;
    align-items: center;
    justify-content: center;
  }
  .brand-name {
    color: var(--logo-text);
    font-family: "Rubik", sans-serif;
    font-weight: 400;
    font-size: 52px;
    letter-spacing: 1px;
  }
  .card-details {
    position: absolute;
    left: 480px;
    top: 118px;
    width: 500px;
  }
  .person-name {
    color: var(--brand-purple);
    font-weight: 500;
    font-size: 46px;
    line-height: 1.1;
    margin-bottom: 14px;
  }
  .credentials,
  .job-title {
    color: var(--text-grey);
    font-weight: 400;
    font-size: 25px;
    line-height: 1.35;
  }
  .contact-list {
    list-style: none;
    margin-top: 30px;
  }
  .contact-item {
    display: flex;
    align-items: center;
    gap: 18px;
    height: 56px;
    color: var(--brand-purple);
    font-size: 23px;
  }
  .contact-icon {
    width: 26px;
    height: 26px;
    flex: none;
    fill: var(--brand-purple);
  }
</style>
</head>
<body>
<main class="canvas">
  <article class="business-card">
    <div class="brand-mark">
      <span class="brand-name">Brightpaths</span>
    </div>

    <section class="card-details">
      <h1 class="person-name">Dorota Valk</h1>
      <p class="credentials">CCC-SLP, TSSLD</p>
      <p class="job-title">Speech Language Pathologist</p>

      <ul class="contact-list">
        <li class="contact-item">
          <svg class="contact-icon" viewBox="0 0 24 24" aria-hidden="true">
            <path d="M2 5h20v14H2z M3.5 6.5 12 13l8.5-6.5" fill="none" stroke="#7a5ea8" stroke-width="2" stroke-linejoin="round"/>
          </svg>
          <span>dorotavalk@brightpathsslp.example</span>
        </li>
        <li class="contact-item">
          <svg class="contact-icon" viewBox="0 0 24 24" aria-hidden="true">
            <circle cx="12" cy="12" r="10"/>
            <path d="M2 12h20 M12 2c3 3 4 6.5 4 10s-1 7-4 10 M12 2c-3 3-4 6.5-4 10s1 7 4 10" fill="none" stroke="#ffffff" stroke-width="1.6"/>
          </svg>
          <span>Brightpathsslp.example</span>
        </li>
        <li class="contact-item">
          <svg class="contact-icon" viewBox="0 0 24 24" aria-hidden="true">
            <path d="M6.6 10.8c1.4 2.8 3.8 5.1 6.6 6.6l2.2-2.2c.3-.3.7-.4 1-.2 1.1.4 2.3.6 3.6.6.6 0 1 .4 1 1V20c0 .6-.4 1-1 1C10.6 21 3 13.4 3 4c0-.6.4-1 1-1h3.5c.6 0 1 .4 1 1 0 1.3.2 2.5.6 3.6.1.3 0 .7-.2 1z"/>
          </svg>
          <span>(555) 271-8390</span>
        </li>
      </ul>
    </section>
  </article>
</main>
</body>
</html>
```